Industrial Laundry News Paper Add

We need a color add for 1/4 page newspaper using blue and white. We are an industrial laundry providing linen washing for condo rental companies. We can provide linen rental and wash customer-owned goods

```html
<!DOCTYPE html>
<html lang="en">
<head>
<meta charset="utf-8">
<title>Summit Ridge Services – Industrial Laundry</title>
<link href="https://fonts.googleapis.com/css2?family=Source+Sans+3:wght@400;600;700&display=swap" rel="stylesheet">
<style>
  :root {
    --navy: #1f3b7a;
    --blue-deep: #1b4f9e;
    --blue-mid: #2a6cc0;
    --blue-glow: #3e93dc;
    --blue-light: #8fc3ea;
    --white: #ffffff;
    --photo-dark: #5b6068;
    --photo-light: #c9ccd0;
    --ink: #1c2a4a;
  }
  * { margin: 0; padding: 0; box-sizing: border-box; }
  html, body { width: 960px; height: 1200px; overflow: hidden; background: #ffffff; }
  .ad {
    position: relative;
    width: 960px;
    height: 1200px;
    font-family: "Source Sans 3", "Helvetica Neue", Arial, sans-serif;
    color: var(--white);
    overflow: hidden;
  }
  .ad__photo {
    position: absolute;
    left: 0; top: 0;
    width: 960px; height: 520px;
    background: linear-gradient(115deg, var(--photo-light) 0%, #9ea3aa 35%, var(--photo-dark) 70%, #3c4047 100%);
  }
  .ad__bands { position: absolute; left: 0; top: 0; width: 960px; height: 1200px; }
  .ad__headline {
    position: absolute;
    top: 540px; left: 0; width: 960px;
    text-align: center;
    font-size: 46px;
    font-weight: 700;
    text-shadow: 0 2px 6px rgba(0,0,0,0.35);
  }
  .ad__body {
    position: absolute;
    top: 618px; left: 0; width: 960px;
    text-align: center;
    font-size: 31px;
    line-height: 42px;
    font-weight: 400;
    text-shadow: 0 1px 4px rgba(0,0,0,0.3);
  }
  .ad__services {
    position: absolute;
    top: 770px; left: 0; width: 960px;
    display: flex; justify-content: center; gap: 52px;
  }
  .service-icon {
    width: 92px; height: 92px;
    background: var(--white);
    border-radius: 10px;
    display: flex; align-items: center; justify-content: center;
    box-shadow: 0 2px 6px rgba(0,0,0,0.25);
  }
  .service-icon svg { width: 66px; height: 66px; }
  .ad__brand {
    position: absolute;
    left: 60px; top: 1040px;
    color: var(--navy);
    font-weight: 700;
    font-size: 50px;
    line-height: 54px;
    letter-spacing: 1px;
    text-transform: uppercase;
  }
  .ad__contact {
    position: absolute;
    right: 44px; top: 1030px;
    list-style: none;
    color: var(--ink);
    font-size: 25px;
    font-weight: 600;
  }
  .contact-item {
    display: flex; align-items: center; justify-content: flex-end;
    gap: 14px; height: 44px;
  }
  .contact-item__icon {
    width: 30px; height: 30px;
    background: var(--navy);
    border-radius: 5px;
    display: flex; align-items: center; justify-content: center;
  }
  .contact-item__icon svg { width: 20px; height: 20px; }
</style>
</head>
<body>
<main class="ad">
  <div class="ad__photo" role="img" aria-label="Photograph of a row of stainless steel industrial front-loading washing machines with one door open"></div>

  <svg class="ad__bands" viewBox="0 0 960 1200" aria-hidden="true">
    <defs>
      <radialGradient id="bandGlow" cx="0.5" cy="0.45" r="0.6">
        <stop offset="0" stop-color="#3e93dc"/>
        <stop offset="0.55" stop-color="#2a6cc0"/>
        <stop offset="1" stop-color="#1b4f9e"/>
      </radialGradient>
    </defs>
    <path d="M0 455 C 250 425, 520 520, 960 378 L960 1200 L0 1200 Z" fill="#8fc3ea"/>
    <path d="M0 482 C 260 452, 540 548, 960 410 L960 1200 L0 1200 Z" fill="url(#bandGlow)"/>
    <path d="M0 928 C 300 990, 620 878, 960 786 L960 1200 L0 1200 Z" fill="#8fc3ea"/>
    <path d="M0 956 C 300 1012, 640 904, 960 816 L960 1200 L0 1200 Z" fill="#ffffff"/>
  </svg>

  <h1 class="ad__headline">The First Name In Industrial Laundry</h1>
  <p class="ad__body">
    We are an industrial laundry providing linen washing<br>
    for condo rental companies.<br>
    We can provide linen rental and wash customer-owned goods
  </p>

  <div class="ad__services">
    <div class="service-icon" aria-label="Dining and table linens">
      <svg viewBox="0 0 66 66" fill="none" stroke="#1f3b7a" stroke-width="3.5" stroke-linecap="round">
        <path d="M14 28 H52 M18 28 V48 M48 28 V48"/>
        <path d="M6 22 V48 M6 38 H13 V48"/>
        <path d="M60 22 V48 M60 38 H53 V48"/>
        <path d="M24 22 H42"/>
      </svg>
    </div>
    <div class="service-icon" aria-label="Folded linen stack">
      <svg viewBox="0 0 66 66" fill="#1f3b7a">
        <rect x="12" y="16" width="42" height="9" rx="3"/>
        <rect x="9" y="28" width="48" height="9" rx="3"/>
        <rect x="12" y="40" width="42" height="9" rx="3"/>
      </svg>
    </div>
    <div class="service-icon" aria-label="Garment on hanger">
      <svg viewBox="0 0 66 66" fill="none" stroke="#1f3b7a" stroke-width="3.5" stroke-linecap="round" stroke-linejoin="round">
        <path d="M28 14 a5 5 0 1 1 5 5 V23"/>
        <path d="M10 32 L33 23 L56 32"/>
        <path d="M18 30 H48 V54 H18 Z" fill="#1f3b7a"/>
      </svg>
    </div>
  </div>

  <div class="ad__brand">Summit Ridge<br>Services</div>

  <ul class="ad__contact">
    <li class="contact-item">+1.5550142870
      <span class="contact-item__icon"><svg viewBox="0 0 20 20" fill="#fff"><path d="M5 2 L8 2 L9 6 L7 8 C8 10.5 9.5 12 12 13 L14 11 L18 12 L18 15 C18 16.5 17 17.5 15.5 17.5 C8.5 17 3 11.5 2.5 4.5 C2.5 3 3.5 2 5 2 Z"/></svg></span>
    </li>
    <li class="contact-item">summitridgeservices.com
      <span class="contact-item__icon"><svg viewBox="0 0 20 20" fill="none" stroke="#fff" stroke-width="1.6"><circle cx="10" cy="10" r="7.5"/><ellipse cx="10" cy="10" rx="3.2" ry="7.5"/><path d="M2.5 10 H17.5"/></svg></span>
    </li>
    <li class="contact-item">Alder Crest, CA 93599, USA
      <span class="contact-item__icon"><svg viewBox="0 0 20 20" fill="#fff"><path d="M10 2 C6.5 2 4 4.6 4 8 C4 12 10 18 10 18 C10 18 16 12 16 8 C16 4.6 13.5 2 10 2 Z M10 10.5 A2.5 2.5 0 1 1 10 5.5 A2.5 2.5 0 1 1 10 10.5 Z"/></svg></span>
    </li>
  </ul>
</main>
</body>
</html>
```